New Year Resolution Infographic

We are a weight loss company that provides holistic, natural nutrition programs to consumers -- you can see our Web site at www.TrimLark.com We need a simple infographic to be shared on social media and via email for New Year's day. The topic for the infographic is "how to set and keep your weight loss resolution". We've outlined 5 process steps for consumers to follow to assist with their weight loss resolutions, and we would like to depict this graphically.

Target Market(s)

Women age 35-65 who are planning to make a resolution to lose weight in the new year.

Industry/Entity Type

Health And Wellness

Font styles to use
Sans Serif

Colors
0392cd
9bcb3c

Requirements
Must have
• Initial graphic showing failure stats (see copy)
• Graphic showing process steps in making/keeping a resolution (see copy)
• TrimLark Logo

```html
<!DOCTYPE html>
<html lang="en">
<head>
<meta charset="utf-8">
<title>Weight Loss Resolution Guide</title>
<link href="https://fonts.googleapis.com/css2?family=Open+Sans:wght@400;600&display=swap" rel="stylesheet">
<style>
  :root {
    --blue: #29a8e0;
    --green: #8cc63f;
    --panel: #e6e6e7;
    --text: #3f3f3f;
    --rule: #9a9a9a;
    --white: #ffffff;
    --art-grey: #8a8a8a;
    --art-orange: #f08a24;
  }
  html, body {
    margin: 0;
    padding: 0;
    width: 1200px;
    height: 1132px;
    overflow: hidden;
    background: var(--white);
    font-family: "Open Sans", Arial, sans-serif;
  }
  .canvas {
    position: relative;
    width: 1200px;
    height: 1132px;
  }
  .intro {
    position: absolute;
    left: 158px;
    top: 42px;
    margin: 0;
    font-size: 46px;
    line-height: 62px;
    font-weight: 600;
    color: var(--blue);
    white-space: nowrap;
  }
  .step {
    position: absolute;
    left: 76px;
    width: 1064px;
    background: var(--panel);
  }
  .step--reflect { top: 264px; height: 408px; }
  .step--resolve { top: 716px; height: 416px; }
  .step__badge {
    position: absolute;
    left: 465px;
    top: -25px;
    width: 42px;
    height: 42px;
    border-radius: 50%;
    border: 4px solid var(--white);
    color: var(--white);
    font-size: 22px;
    font-weight: 600;
    line-height: 42px;
    text-align: center;
  }
  .step--reflect .step__badge { background: var(--green); }
  .step--resolve .step__badge { background: var(--blue); }
  .step__title {
    position: absolute;
    left: 78px;
    margin: 0;
    font-weight: 600;
    line-height: 1.2;
  }
  .step--reflect .step__title { color: var(--green); font-size: 40px; top: 68px; }
  .step--resolve .step__title { color: var(--blue); font-size: 49px; top: 60px; }
  .step__body {
    position: absolute;
    left: 78px;
    margin: 0;
    font-size: 27px;
    line-height: 36px;
    color: var(--text);
    white-space: nowrap;
  }
  .step--reflect .step__body { top: 130px; }
  .step--resolve .step__body { top: 134px; }
  .step__rule {
    position: absolute;
    left: 80px;
    width: 860px;
    height: 4px;
  }
  .step--reflect .step__rule { top: 348px; }
  .step--resolve .step__rule { top: 358px; }
  .step__art {
    position: absolute;
    border-radius: 6px;
  }
  .art--podium {
    left: 604px;
    top: 56px;
    width: 330px;
    height: 280px;
    background: linear-gradient(180deg, var(--art-orange) 0%, var(--art-grey) 100%);
    opacity: 0.85;
  }
  .art--calendar {
    left: 700px;
    top: 84px;
    width: 226px;
    height: 280px;
    background: linear-gradient(180deg, var(--blue) 0%, #b9b9b9 45%, var(--green) 100%);
    opacity: 0.85;
  }
</style>
</head>
<body>
<main class="canvas">
  <h1 class="intro">Here is a quick guide to setting and<br>reaching your weight loss resolution<br>this year.</h1>

  <section class="step step--reflect">
    <div class="step__badge">1</div>
    <h2 class="step__title">Reflect</h2>
    <p class="step__body">Get clear on why the achievement<br>of your resolution is important.<br>You'll need to come back to this if<br>you falter!</p>
    <div class="step__art art--podium" role="img" aria-label="Illustration of three figures on a winners' podium, the centre figure in orange with raised arms"></div>
    <svg class="step__rule" viewBox="0 0 860 4" aria-hidden="true">
      <line x1="0" y1="2" x2="28" y2="2" stroke="var(--rule)" stroke-width="3"/>
      <line x1="48" y1="2" x2="860" y2="2" stroke="var(--rule)" stroke-width="3"/>
    </svg>
  </section>

  <section class="step step--resolve">
    <div class="step__badge">2</div>
    <h2 class="step__title">Resolve</h2>
    <p class="step__body">Set a weight loss goal for the year that<br>is realistic, then break this up into<br>even shorter term goals of 30-60<br>days, with a specific diet and activity<br>plan to guide you.</p>
    <div class="step__art art--calendar" role="img" aria-label="Illustration of a wall calendar being marked by a hand holding a pencil"></div>
    <svg class="step__rule" viewBox="0 0 860 4" aria-hidden="true">
      <line x1="0" y1="2" x2="28" y2="2" stroke="var(--rule)" stroke-width="3"/>
      <line x1="48" y1="2" x2="860" y2="2" stroke="var(--rule)" stroke-width="3"/>
    </svg>
  </section>
</main>
</body>
</html>
```